Recruiting ad for Caregivers and Nurses

We need a few amazing, fun, catchy, creative recruiting ads for Caregivers and Nurses to care for homecare patients on the island of Oahu, in Hawaii. We are an in home care company called Brantley Homecare. Our care services are provided 24/7, so we need staff that can work days, nights, weekdays, weekends. We need catchy fun ads to entice caregivers and nurses to call our office to inquire about jobs available. Our patients age range is from babies to seniors. We need caregivers and nurses for basic patient care (bathing, dressing, ambulating, preparing meals, medication reminders, light housekeeping) and complex patients (oxygen, tube feeding, injections, vents, wound care). Here are some bullets to consider including:
*Full-time and Part-time Positions Available (days, nights, weekdays, weekends)
*Sign-On Bonus Programs Offered up to $500
*Refer a Friend Bonus Program
*Holiday Pay
*2 Health Plans to Choose from
*Island-Wide Locations
*All PPE Provided (masks, gloves, etc)
*401K Program
*Tuition Benefits

```html
<!DOCTYPE html>
<html lang="en">
<head>
<meta charset="utf-8">
<title>Brantley Homecare – We're Hiring</title>
<link rel="stylesheet" href="https://fonts.googleapis.com/css2?family=Montserrat:wght@400;500;600;700;800;900&display=swap">
<style>
  :root {
    --teal: #007a73;
    --orange: #ee7a55;
    --ink: #1f2a2e;
    --paper: #ffffff;
    --stage: #34373b;
    --rule: #b9d6d3;
    --sky-top: #4f6fae;
    --sky-mid: #a9bfe0;
    --sky-warm: #f3dcc0;
  }
  * { box-sizing: border-box; margin: 0; padding: 0; }
  html, body { width: 1200px; height: 1077px; overflow: hidden; }
  body {
    background: var(--stage);
    font-family: "Montserrat", sans-serif;
    color: var(--ink);
    position: relative;
  }
  .ad {
    position: absolute;
    left: 200px; top: 21px;
    width: 800px; height: 1035px;
    background: var(--paper);
    overflow: hidden;
  }
  .scenery {
    position: absolute; left: 0; top: 0; width: 800px; height: 520px;
    background:
      linear-gradient(180deg, rgba(255,255,255,0) 60%, #fff 100%),
      linear-gradient(180deg, var(--sky-top) 0%, var(--sky-mid) 45%, var(--sky-warm) 80%, #f6efe6 100%);
  }
  .staff-photo {
    position: absolute; left: 360px; top: 120px; width: 440px; height: 470px;
    background: radial-gradient(ellipse at 55% 45%, #d9e4f2 0%, #eef2f7 45%, rgba(255,255,255,0) 72%);
  }
  .brand {
    position: absolute; left: 56px; top: 150px;
    width: 200px; height: 130px;
    background: var(--paper);
    display: flex; flex-direction: column; align-items: center; justify-content: center; gap: 10px;
    box-shadow: 0 2px 8px rgba(0,0,0,.12);
  }
  .brand-mark { width: 30px; height: 30px; background: var(--orange); }
  .brand-name {
    font-weight: 700; font-size: 21px; color: var(--teal);
    text-align: center; line-height: 1.15;
  }
  .headline { position: absolute; left: 96px; top: 318px; color: var(--teal); }
  .headline .lead { display: block; font-weight: 900; font-size: 52px; line-height: 1; margin-left: 10px; }
  .headline .main { display: block; font-weight: 900; font-size: 158px; line-height: .9; letter-spacing: -3px; }
  .swoosh { position: absolute; left: 20px; top: 500px; }
  .positions { position: absolute; left: 120px; top: 580px; color: var(--teal); }
  .positions .kind { display: block; font-weight: 500; font-size: 22px; letter-spacing: .5px; }
  .positions .title { display: block; font-weight: 900; font-size: 46px; line-height: 1; }
  .benefits {
    position: absolute; list-style: none;
    display: flex; flex-direction: column; gap: 22px;
  }
  .benefits.primary { left: 100px; top: 730px; width: 260px; }
  .benefits.secondary { left: 425px; top: 612px; width: 180px; padding-left: 18px; border-left: 1.5px solid var(--rule); }
  .benefit { display: flex; align-items: center; gap: 12px; font-weight: 600; font-size: 15px; line-height: 1.2; }
  .benefit svg { flex: 0 0 40px; width: 40px; height: 40px; }
  .contact { position: absolute; left: 625px; top: 612px; width: 150px; }
  .contact h2 { color: var(--teal); font-weight: 800; font-size: 20px; line-height: 1.1; }
  .contact .rule { display: block; width: 140px; height: 4px; background: var(--orange); margin: 14px 0 16px; }
  .contact p { font-weight: 700; font-size: 16px; margin-bottom: 8px; display: flex; align-items: center; gap: 6px; white-space: nowrap; }
  .contact p.web { font-size: 12.5px; }
  .footer-band { position: absolute; left: 0; bottom: 0; width: 800px; height: 24px; background: var(--teal); border-top: 4px solid var(--paper); box-shadow: 0 -2px 0 var(--teal); }
</style>
</head>
<body>
  <article class="ad">
    <div class="scenery" role="img" aria-label="Tropical sky with scattered clouds and palm trees above a beach"></div>
    <div class="staff-photo" role="img" aria-label="Smiling team of nurses and a doctor in scrubs, one nurse pointing forward"></div>

    <div class="brand">
      <span class="brand-mark"></span>
      <span class="brand-name">Brantley<br>Homecare</span>
    </div>

    <h1 class="headline">
      <span class="lead">WE'RE</span>
      <span class="main">HIRING</span>
    </h1>

    <svg class="swoosh" width="420" height="70" viewBox="0 0 420 70">
      <path d="M4 64 Q 200 22 416 2 Q 200 32 10 70 Z" fill="var(--orange)"/>
    </svg>

    <div class="positions">
      <span class="kind">FULL-TIME &amp; PART-TIME</span>
      <span class="title">POSITIONS</span>
      <span class="title">AVAILABLE</span>
    </div>

    <ul class="benefits primary">
      <li class="benefit">
        <svg viewBox="0 0 44 44" fill="none" stroke="var(--orange)" stroke-width="2"><circle cx="22" cy="18" r="14"/><path d="M14 30 L10 42 L16 39 L19 43 L22 32"/><path d="M30 30 L34 42 L28 39 L25 43 L22 32"/></svg>
        <span>Sign-On Bonus Programs Offered up to $500</span>
      </li>
      <li class="benefit">
        <svg viewBox="0 0 44 44" fill="none" stroke="var(--orange)" stroke-width="2"><rect x="8" y="6" width="26" height="34" rx="2"/><rect x="15" y="3" width="12" height="6"/><path d="M13 16h16M13 23h16M13 30h10"/></svg>
        <span>2 Health Plans to Choose from</span>
      </li>
      <li class="benefit">
        <svg viewBox="0 0 44 44" fill="none" stroke="var(--orange)" stroke-width="2"><path d="M8 16 Q22 10 36 16 L34 30 Q22 38 10 30 Z"/><path d="M8 18 L3 16 M36 18 L41 16 M10 28 L4 30 M34 28 L40 30 M14 20h16M14 25h16"/></svg>
        <span>All PPE Provided (masks, gloves, etc)</span>
      </li>
      <li class="benefit">
        <svg viewBox="0 0 44 44" fill="none" stroke="var(--orange)" stroke-width="2"><rect x="5" y="9" width="34" height="30" rx="2"/><path d="M5 17h34M13 5v8M31 5v8"/></svg>
        <span>Holiday Pay</span>
      </li>
    </ul>

    <ul class="benefits secondary">
      <li class="benefit">
        <svg viewBox="0 0 44 44" fill="none" stroke="var(--orange)" stroke-width="2.4"><circle cx="18" cy="14" r="9"/><path d="M6 40 Q8 26 18 24"/><path d="M26 36 Q34 34 36 26 M32 28l4-3 3 4"/></svg>
        <span>Refer a Friend Bonus Program</span>
      </li>
      <li class="benefit">
        <svg viewBox="0 0 44 44" fill="none" stroke="var(--orange)" stroke-width="2"><path d="M4 36 Q22 28 40 36"/><path d="M20 32 Q21 20 18 12"/><path d="M18 12 Q10 8 6 14 M18 12 Q26 8 30 14 M18 12 Q16 4 10 4 M18 12 Q22 4 28 5"/></svg>
        <span>Island-Wide Locations</span>
      </li>
      <li class="benefit">
        <svg viewBox="0 0 44 44" fill="none" stroke="var(--orange)" stroke-width="2"><path d="M2 18 L22 10 L42 18 L22 26 Z"/><path d="M11 22 V32 Q22 38 33 32 V22"/><path d="M40 19 V30"/></svg>
        <span>Tuition Benefits</span>
      </li>
      <li class="benefit">
        <svg viewBox="0 0 44 44" fill="none" stroke="var(--orange)" stroke-width="2"><circle cx="24" cy="14" r="9"/><path d="M24 10v8M21 12h5"/><path d="M4 34 L14 28 Q20 26 26 30 L36 28 Q40 29 36 33 L22 40 L8 40"/></svg>
        <span>401K Program</span>
      </li>
    </ul>

    <aside class="contact">
      <h2>CONTACT US FOR MORE INFORMATION</h2>
      <span class="rule"></span>
      <p><svg width="14" height="14" viewBox="0 0 14 14"><path d="M3 1 L5 4 L4 6 Q6 9 8 10 L10 9 L13 11 L11 13 Q4 12 1 3 Z" fill="var(--teal)"/></svg>808-555-0142</p>
      <p class="web"><svg width="9" height="9" viewBox="0 0 10 10"><circle cx="5" cy="5" r="5" fill="var(--teal)"/></svg>www.brantleycare.com</p>
    </aside>

    <div class="footer-band"></div>
  </article>
</body>
</html>
```